Teaching Tool Design

This is a teaching evaluating tool so that teachers can assess how well they are teaching.
Please use the Stepwise Lesson Teaching Review Grid as the text for the project.
Design a clean, visually aligned version of the Stepwise Lesson Review Grid that reflects Talwyn’s instructional model and KIVU’s framework https://www.learnprobe.example.au/sites/default/files/2022-08/stepwise-lesson-grid-a2.pdf
Use a professional layout with clear column divisions, alternating row shading, and space for observer notes and teacher reflection.
Copy Talwyn's style theme https://talwynhs.qx.example.au/
Also please see the attached to make a similar style.

```html
<!DOCTYPE html>
<html lang="en">
<head>
<meta charset="utf-8">
<title>Stepwise lesson review grid</title>
<link href="https://fonts.googleapis.com/css2?family=Poppins:wght@500;600;700&family=Montserrat:wght@400;500;600;700&display=swap" rel="stylesheet">
<style>
:root{
  --navy:#1d3679;
  --yellow:#f4e36c;
  --yellow-soft:#fbf0b4;
  --cream:#fdf6da;
  --cream-2:#fcf2c7;
  --ind-yellow:#f8e8a2;
  --grey:#efefef;
  --grey-ind:#e4e4e4;
  --grey-cap:#d8d8d8;
  --blue:#d9e5f4;
  --blue-ind:#cbdaee;
  --board:#8b8b8b;
  --ink:#1c1c1c;
  --teal:#1b8b96;
  --page-tint:#f3f4f7;
}
*{box-sizing:border-box;margin:0;padding:0}
html,body{width:846px;height:1200px;overflow:hidden}
body{background:var(--board);font-family:"Montserrat",sans-serif;color:var(--ink);position:relative}
.page-label{position:absolute;color:#fff;font-family:"Poppins",sans-serif;font-weight:700;font-size:14px;letter-spacing:7px}
.page{position:absolute;background:#fff;overflow:hidden}
.p1{left:48px;top:50px;width:362px;height:524px;background:var(--page-tint)}
.p2{left:439px;top:50px;width:363px;height:524px}
.p3{left:48px;top:631px;width:756px;height:520px}

.org-strip{position:absolute;top:18px;right:0;font-size:5.6px;display:flex;align-items:center;gap:6px;color:#222}
.org-strip i{display:block;width:18px;height:5px;background:var(--navy);border-left:3px solid var(--yellow)}
.page-foot{position:absolute;left:0;bottom:0;width:100%;height:24px;background:var(--navy);color:#fff;display:flex;align-items:center;justify-content:space-between;padding:0 15px 0 22px;font-size:6.4px}
.page-foot .site{font-weight:700;display:flex;align-items:center;gap:3px}
.page-foot svg.stripes{position:absolute;right:40px;top:0}
.page-foot .num{position:relative;font-weight:500}

/* page 1 */
.brand{position:absolute;left:22px;top:16px;display:flex;align-items:center;gap:5px}
.brand .dot{width:14px;height:14px;border-radius:50%;background:var(--teal)}
.brand .name{font-family:"Poppins",sans-serif;font-weight:600;color:var(--navy);font-size:10px;line-height:1.05;width:80px}
.title-band{position:absolute;left:0;top:72px;width:100%;height:46px;background:var(--navy)}
.title-band h1{font-family:"Poppins",sans-serif;font-weight:700;color:#fff;font-size:19.5px;position:absolute;left:31px;top:7px;letter-spacing:-.2px}
.title-band h1 em,.p3-foot h2 em,h2 em{font-style:normal}
.title-band h1 em{color:var(--yellow)}
.callout{position:absolute;left:25px;top:118px;width:320px;height:58px;background:var(--yellow);border-radius:0 0 10px 10px;padding:9px 18px;font-size:8.2px;line-height:1.2;color:var(--navy)}
.callout p+p{margin-top:4px}
.callout b{font-weight:700;text-decoration:underline}
.callout:before{content:"";position:absolute;left:150px;top:-1px;border:6px solid transparent;border-top-color:var(--navy)}
.p1 h2,.p2 h2{font-family:"Poppins",sans-serif;font-weight:600;font-size:13px;color:#111}
.p1 h2 em,.p2 h2 em{color:var(--navy)}
.txt{font-size:6.6px;line-height:1.18;color:#222}
.how{position:absolute;left:30px;top:184px;width:312px}
.how h2{margin-bottom:3px}
.lower{position:absolute;left:0;top:262px;width:100%;height:240px;background:#fff}
.pill{position:absolute;left:28px;top:264px;height:24px;padding:0 12px;background:var(--navy);border-radius:12px;color:var(--yellow);font-family:"Poppins",sans-serif;font-weight:600;font-size:12px;line-height:24px}
.start-intro{position:absolute;left:30px;top:293px;width:310px}
.step{position:absolute;left:30px;width:322px;display:flex;gap:8px}
.step .txt{font-size:6.2px;line-height:1.2}
.step .ring{flex:none;width:34px;height:34px;border:1px dashed var(--navy);border-radius:50%;position:relative}
.step .ring b{position:absolute;right:-2px;top:-4px;width:12px;height:12px;border-radius:50%;background:var(--yellow);font-size:6px;color:var(--navy);text-align:center;line-height:12px;font-weight:700}
.step .ring svg{position:absolute;left:9px;top:9px}
.steps-line{position:absolute;left:47px;top:353px;height:112px;border-left:1px dashed var(--navy)}

/* page 2 */
.p2 .doc-name{position:absolute;left:25px;top:18px;font-size:5.8px;color:var(--navy)}
.diagram{position:absolute;left:85px;top:40px;display:grid;grid-template-columns:39px 60px 59px;grid-template-rows:17px 39px 20px 33px 24px 15px 25px 13px;font-size:3.8px;line-height:1.15}
.diagram div{border:.5px solid #555;padding:2px 3px;background:#fff}
.diagram .side{background:var(--navy);color:#fff;border-color:var(--navy)}
.diagram .hl{background:var(--yellow)}
.diagram .ind{background:var(--navy);color:#fff;border-color:#fff}
.diagram .cap{grid-column:2/4;background:var(--navy);color:#fff;display:flex;align-items:center;gap:3px;border-color:#fff}
.diagram .cap span{width:7px;height:7px;border-radius:50%;background:var(--yellow);flex:none}
.note{position:absolute;background:var(--navy);color:#fff;border:1px solid var(--yellow);font-size:3.8px;line-height:1.2;padding:4px}
.note.light{background:#fff;color:var(--navy);font-weight:600}
.why{position:absolute;left:23px;top:242px;width:320px}
.why h2{margin-bottom:4px}
.ways{position:absolute;left:23px;top:318px;width:325px}
.tag{display:inline-flex;align-items:center;gap:4px;background:var(--yellow);border-radius:7px;padding:2px 6px;font-family:"Poppins",sans-serif;font-weight:600;font-size:8.4px;color:var(--navy);margin:5px 0 4px}
.tag i{width:9px;height:9px;border-radius:50%;background:var(--navy);display:inline-block;position:relative}
.tag i:after{content:"";position:absolute;left:2.5px;top:1.5px;width:2.5px;height:4.5px;border:solid #fff;border-width:0 1.2px 1.2px 0;transform:rotate(45deg)}
.ways ul{list-style:none;font-size:5.1px;line-height:1.2;padding-left:7px}
.ways li{position:relative;padding-left:8px}
.ways li:before{content:"→";position:absolute;left:0;color:var(--navy);font-weight:700}
.copy{position:absolute;left:23px;top:488px;font-size:4.6px;color:#444}

/* page 3 grid */
.grid{position:absolute;left:21px;top:16px;width:705px;height:442px;display:grid;grid-template-columns:53px 76px 57px 63px 52px 54px 63px 63px 55px 54px 61px 54px;grid-template-rows:71px 82px 91px 53px 72px 40px 33px;gap:1.2px;background:#fff;font-size:5.3px;line-height:1.1}
.grid > div{padding:6px 7px 4px 8px}
.grid .side{background:var(--navy);color:#fff;font-family:"Poppins",sans-serif;font-weight:500;font-size:8.4px;display:flex;align-items:flex-end;line-height:1.1;padding:6px}
.grid .side.q{grid-column:1;grid-row:1/6}
.grid .side.q svg{margin-left:6px;margin-bottom:2px}
.c1,.c3,.c4,.c6{background:var(--cream)}
.c2,.c5{background:var(--cream-2)}
.c7,.c8,.c9{background:var(--grey)}
.c10,.c11{background:var(--blue)}
.grid .ind.cy{background:var(--ind-yellow)}
.grid .ind.cg{background:var(--grey-ind)}
.grid .ind.cb{background:var(--blue-ind)}
.grid .ind{padding-top:9px}
.small{font-size:4.4px}
.capab{display:flex;align-items:center;gap:7px;font-size:6.1px;line-height:1.05}
.capab b{flex:none;width:16px;height:16px;border-radius:50%;background:#fff;color:var(--navy);font-family:"Poppins",sans-serif;font-size:9px;text-align:center;line-height:16px;font-weight:600}
.capab.y{grid-column:span 3;background:var(--yellow-soft)}
.capab.g{grid-column:span 3;background:var(--grey-cap)}
.capab.b{grid-column:span 2;background:var(--navy);color:#fff}
.p3-foot{position:absolute;left:0;top:470px;width:756px;height:48px;background:var(--navy);color:#fff}
.p3-foot h2{position:absolute;left:21px;top:12px;font-family:"Poppins",sans-serif;font-weight:700;font-size:17.5px}
.p3-foot h2 em{color:var(--yellow)}
.p3-foot .rule{position:absolute;left:267px;top:10px;height:28px;border-left:1px solid #fff}
.p3-foot p{position:absolute;left:277px;top:13px;font-size:8.1px;line-height:1.2;width:270px}
.p3-brand{position:absolute;right:0;top:462px;width:148px;height:58px;background:#fff;display:flex;align-items:center;gap:6px;padding-left:24px}
.p3-brand .dot{width:16px;height:16px;border-radius:50%;background:var(--teal);flex:none}
.p3-brand .name{font-family:"Poppins",sans-serif;font-weight:600;color:var(--navy);font-size:9.4px;line-height:1.05}
</style>
</head>
<body>

<div class="page-label" style="left:195px;top:28px">PAGE 1</div>
<div class="page-label" style="left:593px;top:28px">PAGE 2</div>
<div class="page-label" style="left:384px;top:598px">PAGE 3</div>

<!-- Page 1 -->
<section class="page p1">
  <div class="brand"><span class="dot"></span><span class="name">Kivu Teaching Research Institute</span></div>
  <div class="org-strip">Kivu Teaching Research Institute <i></i></div>
  <div class="title-band"><h1>Stepwise lesson review <em>grid</em></h1></div>
  <div class="callout">
    <p>For context around the creation and purpose of our grids,<br>please visit the <b>KIVU website.</b></p>
    <p>Already familiar with the instructions? <b>Jump to the grid</b> on page 3.</p>
  </div>
  <div class="how">
    <h2>How to use this <em>grid</em></h2>
    <p class="txt">Our grids outline a set of capabilities to do with an evidence-based practice, and consist of 3 elements: capabilities, indicators and quality criteria. All of the capabilities are drawn from KIVU’s Proven Practice guides on formative assessment and explicit instruction. For each broad capability (along the bottom), there are some indicators just above them that specify different ways the capability is demonstrated. Then, for each indicator there are a set of quality criteria that describe different levels of how well that indicator is being implemented.</p>
  </div>
  <div class="lower"></div>
  <div class="pill">Where to start</div>
  <p class="txt start-intro">This grid focuses on the evidence-based practices of explicit instruction and requires you to work upwards – like climbing a ladder</p>
  <div class="steps-line"></div>
  <div class="step" style="top:319px">
    <div class="ring"><b>01</b><svg width="16" height="16" viewBox="0 0 16 16"><circle cx="8" cy="8" r="6" fill="none" stroke="#1d3679" stroke-width="1.2"/><path d="M8 4.5V8l2.5 1.5" fill="none" stroke="#1d3679" stroke-width="1.2"/></svg></div>
    <p class="txt">Focus on one capability at a time. Read your chosen capability and choose an indicator you would like to work through the criteria for. The criteria describe increasing levels of quality; the higher on the grid, the higher the level of quality and difficulty of implementation.</p>
  </div>
  <div class="step" style="top:362px">
    <div class="ring"><b>02</b><svg width="16" height="16" viewBox="0 0 16 16"><rect x="3" y="2" width="10" height="12" rx="1" fill="none" stroke="#1d3679" stroke-width="1.2"/><path d="M5 6h6M5 9h6M5 12h4" stroke="#1d3679" stroke-width="1"/></svg></div>
    <p class="txt">Start at the bottom criterion for the capability you have chosen to work through. If you are able to demonstrate the first criterion, highlight it and continue to move upwards in the same column and read the next criterion. Keep moving upwards in the same column and highlighting each criterion that matches your current practice. When you reach a criterion that does not yet match your current practice, do not highlight it. This criterion (above the one(s) you have highlighted) outlines the behaviours or activities that you can focus on to further develop your skills and confidence in implementing this evidence-based practice. Similarly, if you are using the grid to observe the practice of a colleague, the criterion directly above your marked observation level should be considered the next step in their skill progression. You can revisit the grids at any time, and aim to mark off each higher criterion as you become more skilled and confident in your practice.</p>
  </div>
  <div class="step" style="top:464px">
    <div class="ring"><b>03</b><svg width="16" height="16" viewBox="0 0 16 16"><circle cx="8" cy="6" r="2" fill="none" stroke="#1d3679" stroke-width="1.2"/><path d="M8 8v6M5 11h6" stroke="#1d3679" stroke-width="1.2"/></svg></div>
    <p class="txt">If you are not currently implementing anything from a particular column, highlight ‘I am yet to include any of these behaviours’. From there, the first criterion in the column is your starting point.</p>
  </div>
  <footer class="page-foot">
    <span class="site"><svg width="7" height="7" viewBox="0 0 10 10"><circle cx="5" cy="5" r="4.3" fill="none" stroke="#fff"/><path d="M1 5h8M5 1c-2 2.5-2 5.5 0 8M5 1c2 2.5 2 5.5 0 8" fill="none" stroke="#fff" stroke-width=".7"/></svg>learnprobe.example.au</span>
    <svg class="stripes" width="40" height="24" viewBox="0 0 40 24"><path d="M0 0h7l14 24h-7z" fill="#f4e36c"/><path d="M9 0h5l14 24h-5z" fill="#9aa86a"/><path d="M16 0h5l14 24h-5z" fill="#4f6178"/></svg>
    <span class="num">PAGE 01</span>
  </footer>
</section>

<!-- Page 2 -->
<section class="page p2">
  <div class="doc-name">Stepwise lesson review grid</div>
  <div class="org-strip">Kivu Teaching Research Institute <i></i></div>

  <div class="diagram">
    <div class="side" style="grid-row:1/6"></div><div></div><div></div>
    <div class="hl"></div><div></div>
    <div></div><div class="hl"></div>
    <div>Plans unit based on learning progression</div><div>Plans for likely challenges for current students</div>
    <div>Consults the curriculum or syllabus to identify the common learning progression in the unit</div><div>Identifies prerequisite knowledge and skills from the curriculum</div>
    <div class="side">Quality criteria</div><div>I am yet to include any of these behaviours</div><div class="hl"></div>
    <div class="side" style="display:flex;align-items:flex-end">Indicator</div><div class="ind">Identifies learning progressions from the curriculum</div><div class="ind">Identifies how knowledge and skills build in relevant learning area</div>
    <div class="side">Capability</div><div class="cap"><span></span>Begin with a deep understanding of what your students need to learn</div>
  </div>
  <div class="note" style="left:60px;top:82px;width:52px;height:69px">The quality criteria are found in the column above the indicator and describe increasing levels of quality; the higher on the grid, the higher the level of quality and difficulty of implementation.</div>
  <div class="note light" style="left:250px;top:59px;width:52px;height:38px">The last criterion in each column is the highest performance outcome for that capability / indicator</div>
  <div class="note light" style="left:250px;top:157px;width:52px;height:69px">If you are not currently implementing anything from a particular column, highlight ‘I am yet to include any of these behaviours’ and the first criterion in the column is your starting point.</div>
  <svg style="position:absolute;left:0;top:0" width="363" height="240" viewBox="0 0 363 240">
    <g fill="none" stroke="#d9c63a" stroke-width=".8">
      <path d="M266 97v7h-23m3-3l-3 3 3 3"/>
      <path d="M250 181h-24m3-3l-3 3 3 3"/>
    </g>
  </svg>

  <div class="why">
    <h2>Why are there gaps in the <em>grid?</em></h2>
    <p class="txt">The criteria across one row of the grid are all aligned at the same level of difficulty. Within one column, there may be a gap between one criterion and the next. This suggests that the next criterion is significantly more difficult to implement than the previous one. The gaps in the grid arise because of a pair-wise comparison, which is the process of comparing one criterion with another to determine their comparative level of difficulty. The same process is repeated with all the criteria in the grid, shifting criteria up or down the grid as required.</p>
  </div>
  <div class="ways">
    <h2>Ways you can use this <em>grid</em></h2>
    <span class="tag"><i></i>Individual reflection</span>
    <ul>
      <li>Reflect on and assess how well you are implementing certain teaching practices and identify clear and actionable next steps to enhance your practice.</li>
      <li>Use them as a tool to record evidence of what you’re doing, your strengths and weaknesses, and what your goals are towards improving your evidence-based practice.</li>
    </ul>
    <span class="tag"><i></i>Collaboration with colleagues</span>
    <ul>
      <li>Ask a colleague to record their observations of your practice and record where you’re up to on the grid.</li>
      <li>Use them as a tool to guide feedback cycles and professional development conversations. For example, as a team, discuss approaches for implementing the next criteria up.</li>
    </ul>
    <span class="tag"><i></i>As a school leader</span>
    <ul>
      <li>The grids allow you to provide targeted and specific feedback about what teachers can do to improve their practice</li>
      <li>Use them to record evidence, reflect on, and plan for whole-school improvement and reporting.</li>
    </ul>
  </div>
  <p class="copy">© 2023 Kivu Teaching Research Institute Ltd (KIVU). CC BY 4.0</p>
  <footer class="page-foot">
    <span class="site"><svg width="7" height="7" viewBox="0 0 10 10"><circle cx="5" cy="5" r="4.3" fill="none" stroke="#fff"/><path d="M1 5h8M5 1c-2 2.5-2 5.5 0 8M5 1c2 2.5 2 5.5 0 8" fill="none" stroke="#fff" stroke-width=".7"/></svg>learnprobe.example.au</span>
    <svg class="stripes" width="40" height="24" viewBox="0 0 40 24"><path d="M0 0h7l14 24h-7z" fill="#f4e36c"/><path d="M9 0h5l14 24h-5z" fill="#9aa86a"/><path d="M16 0h5l14 24h-5z" fill="#4f6178"/></svg>
    <span class="num">PAGE 02</span>
  </footer>
</section>

<!-- Page 3 -->
<section class="page p3">
  <div class="grid">
    <div class="side q">Quality<br>criteria<svg width="6" height="14" viewBox="0 0 6 14"><path d="M3 14V1M.5 3.5L3 1l2.5 2.5" fill="none" stroke="#fff" stroke-width="1"/></svg></div>
    <div class="c1">Anticipates critical points within the learning progression when formatively assessing student learning is most important</div>
    <div class="c2"></div><div class="c3"></div><div class="c4"></div><div class="c5"></div><div class="c6"></div><div class="c7"></div>
    <div class="c8">Provides additional support that ensures students are optimally challenged in their learning</div>
    <div class="c9"></div><div class="c10"></div>
    <div class="c11">Provides immediate feedback that does not reduce cognitive demand</div>

    <div class="c1"></div>
    <div class="c2">Identifies likely challenges and common misconceptions</div>
    <div class="c3">Sequences chunked tasks based on the learning progression and evidence of what students already know and are able to do</div>
    <div class="c4"></div><div class="c5"></div>
    <div class="c6">Refers to learning objectives and success criteria throughout the lesson, particularly when achieved</div>
    <div class="c7">Sequences multiple worked examples to gradually introduce different elements of the task or alternative ways of completing it</div>
    <div class="c8"></div>
    <div class="c9">Gradually removes scaffolding based on evidence of student learning</div>
    <div class="c10">Sequences opportunities for independent practice to gradually deepen students’ understanding of what they have learned</div>
    <div class="c11"></div>

    <div class="c1 small">Plans unit based on learning progression</div>
    <div class="c2"></div>
    <div class="c3">Sequences chunked tasks based on the learning progression</div>
    <div class="c4">Tailors learning objectives from the curriculum for the whole class based on what students already know and are able to do</div>
    <div class="c5">Sets clear success criteria and stretch goals for the whole class</div>
    <div class="c6">Develops student understanding of learning objectives and success criteria</div>
    <div class="c7"></div>
    <div class="c8">Provides additional support based on evidence of what students already know and are able to do</div>
    <div class="c9"></div><div class="c10"></div><div class="c11"></div>

    <div class="c1">Consults the curriculum to identify the common learning progression for the target knowledge and skills</div>
    <div class="c2">Identifies prerequisite knowledge and skills from the curriculum</div>
    <div class="c3">Chunks learning into small, manageable tasks</div>
    <div class="c4">Sets learning objectives from the curriculum for the whole class</div>
    <div class="c5">Sets clear success criteria for the whole class</div>
    <div class="c6">Shares learning objectives and success criteria for students</div>
    <div class="c7">Walks students through all required steps for completing the task using worked examples</div>
    <div class="c8">Explains knowledge and skills needed to complete the task</div>
    <div class="c9">Presents some worked examples with removed steps</div>
    <div class="c10">Provides opportunities for independent practice</div>
    <div class="c11">Provides immediate feedback to students as they practise</div>

    <div class="c1">I am yet to include any of these behaviours in my explicit instruction practice</div>
    <div class="c2">I am yet to include any of these behaviours in my explicit instruction practice</div>
    <div class="c3">I am yet to include any of these behaviours in my explicit instruction practice</div>
    <div class="c4">I am yet to include any of these behaviours in my explicit instruction practice</div>
    <div class="c5">I am yet to include any of these behaviours in my explicit instruction practice</div>
    <div class="c6">I am yet to include any of these behaviours in my explicit instruction practice</div>
    <div class="c7">I am yet to include any of these behaviours in my explicit instruction practice</div>
    <div class="c8">I am yet to include any of these behaviours in my explicit instruction practice</div>
    <div class="c9">I am yet to include any of these behaviours in my explicit instruction practice</div>
    <div class="c10">I am yet to include any of these behaviours in my explicit instruction practice</div>
    <div class="c11">I am yet to include any of these behaviours in my explicit instruction practice</div>

    <div class="side">Indicator</div>
    <div class="ind cy">Identifies learning progressions from the curriculum</div>
    <div class="ind cy">Identifies how knowledge and skills build</div>
    <div class="ind cy">Chunks learning</div>
    <div class="ind cy">Sets learning objectives</div>
    <div class="ind cy">Sets success criteria</div>
    <div class="ind cy">Communicates learning objectives and success criteria</div>
    <div class="ind cg">Uses worked examples</div>
    <div class="ind cg">Provides scaffolding when needed</div>
    <div class="ind cg">Removes scaffolding as needed</div>
    <div class="ind cb">Provides opportunities for independent practice</div>
    <div class="ind cb">Interacts with students during practice</div>

    <div class="side">Capability</div>
    <div class="capab y"><b>1</b>Breaks down complex skills and knowledge into smaller instructional tasks</div>
    <div class="capab y"><b>2</b>Sets clear and measurable learning objectives and success criteria</div>
    <div class="capab g"><b>3</b>Uses worked examples to demonstrate what students need to learn</div>
    <div class="capab b"><b>4</b>Provides opportunities for students to practise what they have learned</div>
  </div>

  <div class="p3-foot">
    <h2>Stepwise lesson review <em>grid</em></h2>
    <span class="rule"></span>
    <p>Read the capability and the related criteria. For each capability, identify which criterion best describes your current practice.</p>
    <svg style="position:absolute;left:570px;top:0" width="50" height="48" viewBox="0 0 50 48"><path d="M0 0h8l20 48h-8z" fill="#f4e36c"/><path d="M11 0h6l20 48h-6z" fill="#9aa86a"/><path d="M20 0h6l20 48h-6z" fill="#4f6178"/></svg>
  </div>
  <div class="p3-brand"><span class="dot"></span><span class="name">Kivu Teaching<br>Research<br>Institute</span></div>
</section>

</body>
</html>
```